Velvet Harbor (A luxury Travel Website)

website text attached in document below

images also attached

feel free to use other images if needed

Target Market(s)

Luxury Seekers and wealthy couples / families

Industry/Entity Type

Luxury Travel

Coding

Coded - Design and coding required

Number of Pages Required

1 page

Requirements
Must have
• A luxury design and easy use.
Nice to have
• Ease of use of page, incorporation of images into the flow of the site

```html
<!DOCTYPE html>
<html lang="en">
<head>
<meta charset="utf-8">
<title>Velvet Harbor — Luxury Travel</title>
<link href="https://fonts.googleapis.com/css2?family=Libre+Baskerville:ital@0;1&family=Barlow:wght@400;500;600&display=swap" rel="stylesheet">
<style>
:root{
  --ink:#25292e;
  --text:#3a3f45;
  --muted:#6c737a;
  --accent:#7fa7c9;
  --accent-dark:#4d6a86;
  --grey-band:#e6e6e6;
  --ice:#eef4f7;
  --line:#b9cde0;
  --star:#f0a23a;
  --white:#fff;
}
*{box-sizing:border-box;margin:0;padding:0}
html,body{width:1200px;height:4107px;overflow:hidden}
body{position:relative;font-family:"Barlow",sans-serif;color:var(--text);background:var(--white)}
.serif{font-family:"Libre Baskerville",serif}
section,header,footer{position:absolute;left:0;width:1200px}
.abs{position:absolute}
.eyebrow{font-size:15px;letter-spacing:3.5px;text-transform:uppercase;color:var(--accent-dark);font-weight:500}
.title{font-family:"Libre Baskerville",serif;font-size:36px;line-height:46px;color:var(--ink);font-weight:400}
.para{font-size:18px;line-height:35px;color:var(--text)}
.btn{background:var(--accent);color:#fff;font-weight:600;font-size:17px;letter-spacing:3.5px;text-transform:uppercase;display:flex;align-items:center;justify-content:center;gap:10px}
.photo{position:absolute}
.icon-circle{position:absolute;border-radius:50%;background:var(--accent);display:flex;align-items:center;justify-content:center}

/* header */
.topbar{top:0;height:70px;background:var(--ink);color:#fff}
.topbar .contact{position:absolute;top:14px;display:flex;gap:14px;align-items:center}
.topbar .contact small{display:block;font-family:"Libre Baskerville",serif;font-size:14px}
.topbar .contact b{font-size:15px;font-weight:600}
.logo-tab{position:absolute;left:443px;top:0;width:344px;height:102px;background:var(--ink);border-radius:0 0 14px 14px;display:flex;align-items:center;justify-content:center}
.brand{font-family:"Barlow",sans-serif;font-weight:500;font-size:28px;letter-spacing:2px;color:var(--accent)}
.topbar .divider{position:absolute;top:18px;width:1px;height:34px;background:#4a5058}

/* hero */
.hero{top:70px;height:568px;background:linear-gradient(180deg,#dfe4e8 0%,#cfd6dc 40%,#9fb3c0 62%,#6a8aa0 80%,#8aa8b8 100%)}
.hero .rule{position:absolute;top:132px;height:1px;background:var(--accent)}
.hero h1{position:absolute;top:150px;left:0;width:1200px;text-align:center;font-family:"Libre Baskerville",serif;font-weight:400;font-size:48px;color:var(--ink)}
.search{position:absolute;left:344px;top:274px;width:510px;height:51px;background:#fff;border:2px solid #fff;display:flex}
.search span{flex:1;padding-left:16px;font-size:16px;color:var(--muted);line-height:47px}
.search .btn{width:142px;height:100%}

/* intro */
.intro{top:638px;height:626px;background:var(--grey-band)}
.frame-line{position:absolute;background:#9aa2aa}

/* hotels */
.hotels{top:1264px;height:848px;background:linear-gradient(180deg,var(--ice) 0,var(--ice) 521px,#fff 521px)}
.hotel{position:absolute;top:328px;width:427px}
.hotel .photo{position:relative;width:427px;height:322px}
.hotel h3{position:absolute;top:350px;left:0;font-family:"Libre Baskerville",serif;font-weight:400;font-size:26px;color:var(--ink);white-space:nowrap}
.hotel h3 i{font-style:normal;color:var(--star);font-size:13px;letter-spacing:2px;vertical-align:middle;margin-left:6px}
.hotel .meta{position:absolute;top:392px;left:0;font-size:17px;color:var(--text)}
.hotel .price{position:absolute;top:351px;right:0;width:110px;height:72px}
.hotel .price .disc{position:absolute;left:16px;top:0;width:72px;height:72px;border-radius:50%;background:var(--ice)}
.hotel .price small{position:absolute;right:0;top:0;font-size:16px}
.hotel .price b{position:absolute;right:0;top:20px;font-family:"Libre Baskerville",serif;font-style:italic;font-weight:400;font-size:26px;color:var(--ink)}
.pager{position:absolute;top:185px;left:947px;width:177px;display:flex;justify-content:space-between;align-items:center;font-size:18px;color:var(--ink)}

/* pricing */
.pricing{top:2112px;height:765px;background:linear-gradient(180deg,var(--ice) 0,var(--ice) 55%,#fff 100%)}
.card{position:absolute;background:#fff;box-shadow:0 4px 18px rgba(60,80,100,.06)}
.card.featured{background:linear-gradient(180deg,#d4e4f2 0%,#8eb3d4 100%)}
.banner{position:absolute;left:20px;top:20px;width:298px;height:51px;background:var(--accent);color:#fff;font-family:"Libre Baskerville",serif;font-size:21px;display:flex;align-items:center;justify-content:center;clip-path:polygon(0 0,100% 0,100% 78%,93% 100%,0 100%)}
.featured .banner{background:var(--accent-dark)}
.card .amount{position:absolute;top:92px;left:0;width:100%;text-align:center;font-family:"Libre Baskerville",serif;font-style:italic;color:var(--ink);font-size:34px}
.card .amount small{font-size:16px}
.card .mark{position:absolute;top:152px;left:50%;transform:translateX(-50%);width:74px;height:12px}
.card ul{position:absolute;top:190px;left:52px;list-style:none}
.card li{font-size:18px;line-height:44px;color:var(--text);position:relative;padding-left:17px}
.card li:before{content:"";position:absolute;left:0;top:17px;border-left:6px solid var(--accent);border-top:5px solid transparent;border-bottom:5px solid transparent}

/* contact */
.contact-sec{top:2877px;height:773px;background:#fff}
.field{position:absolute;width:238px}
.field label{display:block;font-size:16px;color:var(--muted)}
.field .value{position:absolute;top:54px;font-size:16px;color:var(--ink)}
.field .underline{position:absolute;top:75px;left:0;width:100%;height:1.5px;background:var(--line)}

/* footer */
.footer{top:3650px;height:457px;background:var(--ink);color:#fff}
.footer .item{position:absolute;top:181px}
.footer .item small{display:block;font-family:"Libre Baskerville",serif;font-size:16px}
.footer .item b{display:block;font-size:16px;font-weight:500;margin-top:10px}
.footer .vdiv{position:absolute;top:180px;width:1px;height:52px;background:#4a5058}
.footer .hline{position:absolute;left:92px;width:1014px;height:1px;background:#3c424a}
.social{position:absolute;top:4056px;width:14px;height:14px;border-radius:50%;background:#fff}
</style>
</head>
<body>

<header class="topbar">
  <div class="contact" style="left:92px">
    <div class="icon-circle" style="position:relative;width:44px;height:44px">
      <svg width="20" height="16" viewBox="0 0 20 16"><rect x="1" y="1" width="18" height="14" rx="2" fill="none" stroke="#fff" stroke-width="1.6"/><path d="M1 2l9 7 9-7" fill="none" stroke="#fff" stroke-width="1.6"/></svg>
    </div>
    <div><small>Email Us:</small><b>support@velvetharbor.com</b></div>
  </div>
  <div class="divider" style="left:411px"></div>
  <div class="logo-tab"><span class="brand">VELVET HARBOR</span></div>
  <div class="divider" style="left:787px"></div>
  <div class="contact" style="left:944px">
    <div class="icon-circle" style="position:relative;width:44px;height:44px">
      <svg width="20" height="20" viewBox="0 0 24 24"><path d="M5 3h4l2 5-2.5 1.5a11 11 0 0 0 6 6L16 13l5 2v4a2 2 0 0 1-2 2A17 17 0 0 1 3 5a2 2 0 0 1 2-2z" fill="none" stroke="#fff" stroke-width="1.6"/></svg>
    </div>
    <div><small>Call Us:</small><b>1800-555-0142</b></div>
  </div>
</header>

<section class="hero" role="img" aria-label="Couple relaxing in an infinity pool overlooking the sea with palm trees">
  <div class="eyebrow abs" style="top:86px;left:0;width:1200px;text-align:center;color:var(--ink);font-size:17px;letter-spacing:4px">Looking to stay at a 5 star hotel</div>
  <div class="rule" style="left:398px;width:176px"></div>
  <div class="rule" style="left:625px;width:180px"></div>
  <div class="icon-circle" style="left:586px;top:118px;width:28px;height:28px;color:#fff;font-size:13px;font-weight:600">OR</div>
  <h1>to fly business class anywhere?</h1>
  <div class="search"><span>Share a screenshot of your travel plans</span><div class="btn">Browse</div></div>
  <svg class="abs" style="left:62px;top:208px" width="32" height="56" viewBox="0 0 32 56"><path d="M30 2L4 28l26 26" fill="none" stroke="#3a3f45" stroke-width="2.5"/></svg>
  <svg class="abs" style="left:1106px;top:208px" width="32" height="56" viewBox="0 0 32 56"><path d="M2 2l26 26L2 54" fill="none" stroke="#25292e" stroke-width="2.5"/></svg>
</section>

<section class="intro">
  <div class="eyebrow abs" style="left:92px;top:60px">We work directly with</div>
  <h2 class="title abs" style="left:92px;top:80px;width:420px;font-size:36px;line-height:45px">Hotels and airlines to get you the best price, always.</h2>
  <p class="para abs" style="left:92px;top:232px;width:420px">Lorem ipsum dolor sit amet consectetur adipiscing elit, sed do eiusmod tempor incididunt ut labore et dolore magna aliqua. Quis ipsum suspendisse ultric es gravidaisus commodo viverra maecenas.</p>
  <div class="btn abs" style="left:92px;top:396px;width:168px;height:48px">Add here <span style="font-size:22px;letter-spacing:0">+</span></div>

  <div class="frame-line" style="left:1020px;top:116px;width:105px;height:1px"></div>
  <div class="frame-line" style="left:1111px;top:108px;width:1px;height:115px"></div>
  <div class="frame-line" style="left:569px;top:382px;width:1px;height:163px"></div>
  <div class="frame-line" style="left:558px;top:537px;width:96px;height:1px"></div>

  <div class="photo" role="img" aria-label="Traveller reclining in a business class airline seat" style="left:580px;top:92px;width:254px;height:253px;background:linear-gradient(160deg,#b7a79a 0%,#6e4f48 55%,#3a2426 100%)"></div>
  <div class="photo" role="img" aria-label="Hotel bedroom with white bed and leaf-patterned wall" style="left:580px;top:360px;width:254px;height:167px;background:linear-gradient(180deg,#a8b0a4 0%,#c9ccc6 55%,#eef0f0 100%)"></div>
  <div class="photo" role="img" aria-label="Aerial view of a tropical island beach with a seaplane on turquoise water" style="left:853px;top:127px;width:253px;height:400px;background:linear-gradient(170deg,#bfe6ea 0%,#7dd3d6 40%,#3f8a52 70%,#2c6b3a 100%)"></div>
</section>

<section class="hotels">
  <div class="eyebrow abs" style="left:92px;top:90px">The hotels</div>
  <h2 class="title abs" style="left:92px;top:114px">Luxury &amp; comfort</h2>
  <p class="para abs" style="left:92px;top:176px;width:470px">Lorem ipsum dolor sit amet consectetur adipiscing elit sed do eiusmod tempor incididunt ut labore et dolore magna aliqua uis ipsum suspendisse</p>
  <div class="pager">
    <span>Prev</span>
    <svg width="66" height="24" viewBox="0 0 66 24"><path d="M10 2L2 12l8 10" fill="none" stroke="#6c737a" stroke-width="1.5"/><circle cx="20" cy="12" r="2.5" fill="#7fa7c9"/><circle cx="33" cy="12" r="2.5" fill="#7fa7c9"/><circle cx="46" cy="12" r="2.5" fill="#7fa7c9"/><path d="M56 2l8 10-8 10" fill="none" stroke="#6c737a" stroke-width="1.5"/></svg>
    <span>Next</span>
  </div>

  <div class="hotel" style="left:35px">
    <div class="photo" role="img" aria-label="Aerial view of overwater villas on a turquoise lagoon" style="background:linear-gradient(150deg,#5fbfc4 0%,#2b9aa2 45%,#1f6f78 100%)"></div>
    <h3>Superior Hotels<i>★★★★★</i></h3>
    <div class="meta">30 M2 &nbsp;/&nbsp; 2Adults 1 Children</div>
    <div class="price"><div class="disc"></div><small>from</small><b>$299</b></div>
  </div>
  <div class="hotel" style="left:496px">
    <div class="photo" role="img" aria-label="Resort building with pool and palm trees at dusk" style="background:linear-gradient(180deg,#3f78c4 0%,#6a8fb8 45%,#7a5a3e 70%,#2d4f8e 100%)"></div>
    <h3>Serenity Hotel<i>★★★★★</i></h3>
    <div class="meta">30 M2 &nbsp;/&nbsp; 2Adults 1 Children</div>
    <div class="price"><div class="disc"></div><small>from</small><b>$299</b></div>
  </div>
  <div class="hotel" style="left:956px">
    <div class="photo" role="img" aria-label="Thatched resort pavilion beside a pool at sunset" style="background:linear-gradient(180deg,#c9b8a8 0%,#8a6a4e 45%,#9fd3d6 75%,#7ec2c8 100%)"></div>
    <h3>Coral Bay Hotel</h3>
    <div class="meta">30 M2 &nbsp;/&nbsp; 2Adults 1 Children</div>
  </div>
</section>

<section class="pricing">
  <div class="eyebrow abs" style="left:0;top:78px;width:1200px;text-align:center">Pricing</div>
  <h2 class="title abs" style="left:0;top:102px;width:1200px;text-align:center">Our packages</h2>

  <div class="card" style="left:92px;top:186px;width:338px;height:485px">
    <div class="banner">Delux Package</div>
    <div class="amount">$137<small>/night</small></div>
    <svg class="mark" viewBox="0 0 74 12"><path d="M0 1h74" stroke="#b9cde0" stroke-width="1.5"/><path d="M30 1l7 8 7-8z" fill="#7fa7c9"/></svg>
    <ul><li>Booking 3 rooms Min</li><li>30% off in Delux Package</li><li>Resturent (Breakfast)</li><li>Free Pick-up From Airport</li><li>24 Hours Free Wi-fi</li><li>Spa and Swiming Facility</li></ul>
  </div>
  <div class="card featured" style="left:430px;top:179px;width:338px;height:502px">
    <div class="banner" style="top:27px">Special Package</div>
    <div class="amount" style="top:99px">$299<small>/night</small></div>
    <svg class="mark" style="top:159px" viewBox="0 0 74 12"><path d="M0 1h74" stroke="#7fa7c9" stroke-width="1.5"/><path d="M30 1l7 8 7-8z" fill="#4d6a86"/></svg>
    <ul style="top:197px"><li>Booking for 5 days Min</li><li>5% Off in special packag</li><li>Resturent (Breakfast)</li><li>Free Pick-up From Airport</li><li>24 Hours Free Wi-fi</li><li>Spa and Swiming Facility</li></ul>
  </div>
  <div class="card" style="left:768px;top:186px;width:338px;height:485px">
    <div class="banner">Luxury Package</div>
    <div class="amount">$379<small>/night</small></div>
    <svg class="mark" viewBox="0 0 74 12"><path d="M0 1h74" stroke="#b9cde0" stroke-width="1.5"/><path d="M30 1l7 8 7-8z" fill="#7fa7c9"/></svg>
    <ul><li>Booking 2 Rooms for 3 days</li><li>30% off in Delux Package</li><li>Resturent (Breakfast)</li><li>Free Pick-up From Airport</li><li>24 Hours Free Wi-fi</li><li>Spa and Swiming Facility</li></ul>
  </div>
</section>

<section class="contact-sec">
  <div class="frame-line" style="left:389px;top:75px;width:89px;height:1px"></div>
  <div class="frame-line" style="left:473px;top:65px;width:1px;height:246px"></div>
  <div class="photo" role="img" aria-label="Overwater resort villas seen from above" style="left:241px;top:314px;width:282px;height:325px;background:linear-gradient(180deg,#9ccfd6 0%,#3f7f8a 55%,#b44a3a 85%,#7fc2c8 100%)"></div>
  <div class="photo" role="img" aria-label="Smiling couple seated in a private jet cabin" style="left:92px;top:83px;width:369px;height:497px;background:linear-gradient(150deg,#e6d3bc 0%,#b98a5c 40%,#5a3524 75%,#2e2a2c 100%)"></div>

  <div class="eyebrow abs" style="left:593px;top:80px">The more details the better.</div>
  <h2 class="title abs" style="left:593px;top:104px;width:420px">Tell us about your next holiday plans</h2>

  <div class="field" style="left:593px;top:232px"><label>Enter Your Name</label><span class="value">Name</span><div class="underline"></div></div>
  <div class="field" style="left:867px;top:232px"><label>Enter Your Email</label><span class="value">Email</span><div class="underline"></div></div>
  <div class="field" style="left:593px;top:352px"><label>Enter Phone No</label><span class="value">Phone</span><div class="underline"></div></div>
  <div class="field" style="left:867px;top:352px"><label>Enter Subject</label><span class="value">Subject</span><div class="underline"></div></div>
  <div class="field" style="left:593px;top:473px;width:513px"><label>Leave Your Message</label><span class="value">Message</span><div class="underline" style="top:119px"></div></div>

  <div class="btn abs" style="left:593px;top:641px;width:221px;height:48px">Send message
    <svg width="16" height="14" viewBox="0 0 16 14"><path d="M1 7h13M9 2l5 5-5 5" fill="none" stroke="#fff" stroke-width="1.8"/></svg>
  </div>
</section>

<footer class="footer">
  <div class="abs" style="left:0;top:86px;width:1200px;text-align:center"><span class="brand">VELVET HARBOR</span></div>

  <div class="icon-circle" style="left:131px;top:184px;width:54px;height:54px">
    <svg width="22" height="18" viewBox="0 0 20 16"><rect x="1" y="1" width="18" height="14" rx="2" fill="none" stroke="#fff" stroke-width="1.6"/><path d="M1 2l9 7 9-7" fill="none" stroke="#fff" stroke-width="1.6"/></svg>
  </div>
  <div class="item" style="left:202px"><small>Email Us:</small><b>support@velvetharbor.com</b></div>
  <div class="vdiv" style="left:438px"></div>
  <div class="icon-circle" style="left:486px;top:184px;width:54px;height:54px">
    <svg width="20" height="24" viewBox="0 0 20 24"><path d="M10 23s8-8 8-14a8 8 0 0 0-16 0c0 6 8 14 8 14z" fill="none" stroke="#fff" stroke-width="1.6"/><circle cx="10" cy="9" r="3" fill="none" stroke="#fff" stroke-width="1.6"/></svg>
  </div>
  <div class="item" style="left:558px"><small>Address:</small><b>88 Harbour Lane, Level 12, AUS</b></div>
  <div class="vdiv" style="left:851px"></div>
  <div class="icon-circle" style="left:898px;top:184px;width:54px;height:54px">
    <svg width="22" height="22" viewBox="0 0 24 24"><path d="M5 3h4l2 5-2.5 1.5a11 11 0 0 0 6 6L16 13l5 2v4a2 2 0 0 1-2 2A17 17 0 0 1 3 5a2 2 0 0 1 2-2z" fill="none" stroke="#fff" stroke-width="1.6"/></svg>
  </div>
  <div class="item" style="left:961px"><small>Call Us:</small><b>1800-555-0142</b></div>

  <div class="abs serif" style="left:92px;top:316px;font-size:20px">Sign up for latest update on your phone:</div>
  <div class="abs" style="left:594px;top:303px;width:512px;height:51px;background:#fff;display:flex;padding:3px">
    <span style="flex:1;padding-left:14px;line-height:45px;font-size:16px;color:var(--muted)">Enter Your Email Address..</span>
    <div class="btn" style="width:166px;height:45px">Subscribe</div>
  </div>
  <div class="hline" style="top:380px"></div>
  <div class="abs" style="left:92px;top:402px;font-size:16px">© 2022 Velvet Harbor.com.au</div>
</footer>
<div class="social" style="left:983px"></div>
<div class="social" style="left:1035px"></div>
<div class="social" style="left:1091px"></div>

</body>
</html>
```